Pricing and Packages Page

#1 Just looking for a design no coding
We Are looking for a Design of the PRICING AND PACKAGES page. The home page is just for reference material.
Winner will be contacted and possibly hired to do additional jobs.
Brivo Real Estate needs a web page design for our bundles. We need it to be visually appeal and an emphasis placed on the premium bundle. Attached are some pngs of our current page, and a paint mock up of an idea of our layout. Please try and stay within the theme of the top menu bars of the paint file. Whites, Blues, Oranges, and Light Grays would be preferred.
Provided is a mock-up of our home screen. We want easy to read yet an initiative for people to select home listing packages on our website. Possible reference websites would be dwellmart.example and listyourplace.example or any website that has packages and pricing to choose from.
The top of the page should include the title Packages & Pricing.
Below that we want to have it easily read and illustrated that the will "Pay Nothing Until Home Sold"
Next to that a space to enter a anticipated sales price, asking the question, how much will you save. Much sure this is emphasized.
Include the bundles, which are separated into three packages, Basic, Premium and Multi-List Package. Please include the Bundle Prices of $179, $249 and $499 along with + Transaction Coordination Fee $299. Have a spot for a Get Started Button.
The boxes on the side are just an example of what to include with the prices.
Transaction Coordination Fee and All Listings Include, We just want the text display in a way where the page isnt text heavy but illustrated.
Additional Services Offered, Just a basic list with prices next to it.
Paint

```html
<!DOCTYPE html>
<html lang="en">
<head>
<meta charset="utf-8">
<title>Packages &amp; Pricing – Brivo Real Estate</title>
<link href="https://fonts.googleapis.com/css2?family=Roboto+Condensed:wght@400;700&family=Roboto:wght@400;500;700&display=swap" rel="stylesheet">
<style>
:root{
  --blue:#1d59a6;
  --navy:#154a91;
  --deep:#0f3f80;
  --orange:#f08a2c;
  --orange-dark:#e0741a;
  --light:#f4f4f4;
  --band:#ececec;
  --line:#d6d6d6;
  --text:#555;
  --muted:#888;
  --white:#fff;
}
*{box-sizing:border-box;margin:0;padding:0}
html,body{width:1200px;height:2866px;overflow:hidden}
body{position:relative;background:var(--white);font-family:"Roboto",Arial,sans-serif;color:var(--text)}
.abs{position:absolute}
.cond{font-family:"Roboto Condensed","Arial Narrow",sans-serif}

/* top nav */
.topbar{left:0;top:0;width:1200px;height:37px;background:var(--navy);display:flex;align-items:center;color:var(--white);font-size:13px;text-transform:uppercase}
.topbar .menu{display:flex;gap:42px;margin-left:56px}
.topbar .phone{margin-left:auto;font-weight:700;font-size:15px;margin-right:22px}
.topbar .help{background:var(--orange);height:37px;display:flex;align-items:center;padding:0 28px;margin-right:53px}
.header{left:0;top:37px;width:1200px;height:78px;background:var(--white)}
.brand{left:58px;top:22px;display:flex;align-items:center;gap:10px;font-size:28px;font-weight:500;color:var(--navy)}
.brand .mark{width:34px;height:34px;background:var(--orange);border-radius:4px}
.user{left:975px;top:16px;width:168px;height:40px;background:#e6e6e6;border-radius:4px;display:flex;align-items:center;gap:12px;padding-left:4px;font-size:14px;font-weight:700;color:#333}
.user .avatar{width:40px;height:40px;border-radius:50%;background:radial-gradient(#9a7a64,#4b3a30)}
.user .caret{margin-left:auto;margin-right:12px;border:5px solid transparent;border-top-color:#555;margin-top:5px}
.titleband{left:0;top:115px;width:1200px;height:126px;background:linear-gradient(#e7ebf1,#f7f8fa)}
.titleband h1{position:absolute;left:118px;top:36px;font-size:46px;color:var(--navy);font-weight:700}
.skyline{position:absolute;left:458px;top:14px;width:640px;height:112px;background:linear-gradient(#c5d6ec,#9fbbe0)}

/* intro boxes */
.box{border:1px solid var(--line);background:var(--light)}
.box h2{font-size:22px;font-weight:400;color:var(--blue);padding:10px 24px;border-bottom:1px solid var(--line);background:var(--white)}
.pay{left:118px;top:287px;width:360px;height:235px}
.pay .zero{position:absolute;left:18px;top:60px;font-size:150px;line-height:1;color:var(--orange);font-weight:400}
.pay .note{position:absolute;left:172px;top:72px;font-size:35px;line-height:44px;color:#555}
.save{left:525px;top:287px;width:555px;height:235px}
.save .q{position:absolute;left:24px;top:62px;font-size:16px}
.save .field{position:absolute;top:98px;width:240px;height:38px;background:var(--white);border:1px solid var(--line);font-size:13px;font-style:italic;color:var(--muted);padding:10px 12px}
.save .hint{position:absolute;left:24px;top:155px;font-size:16px}

/* banner */
.banner{left:118px;top:568px;width:962px;height:105px}
.banner svg{position:absolute;left:0;top:0}
.banner .cell{position:absolute;top:0;height:105px;color:var(--white);display:flex;flex-direction:column;align-items:center;justify-content:center}
.banner .best{left:0;width:250px;font-size:44px}
.banner .plan{font-size:46px;font-weight:700}
.banner .fee{font-size:12px;font-weight:700}

/* comparison table */
.compare{left:118px;top:709px;width:962px;height:419px;border:1px solid var(--line)}
.compare .head{height:38px;background:var(--navy);color:var(--white);font-size:17px;padding:10px 16px;font-weight:500}
.rows{position:absolute;left:0;top:133px;width:960px}
.row{height:35px;display:flex;font-size:12px;color:#444}
.row:nth-child(odd){background:#e2e2e2}
.row:nth-child(even){background:#f4f4f4}
.row .label{width:417px;padding:11px 16px;white-space:nowrap}
.row .c{width:181px;text-align:center;padding-top:10px;color:var(--orange-dark);font-weight:700}
.row .c.t{color:#444;font-weight:400}
.col-head{position:absolute;top:38px;width:181px;text-align:center}
.col-head .name{height:33px;background:var(--orange);color:var(--white);font-size:17px;padding-top:7px}
.col-head .price{height:61px;background:linear-gradient(#444,#111);color:var(--white);font-size:24px;font-weight:700;padding-top:17px}
.premium-col{left:716px;top:738px;width:182px;height:395px;background:#efefef;box-shadow:0 2px 14px rgba(0,0,0,.35);z-index:2;text-align:center}
.premium-col .name{height:42px;background:linear-gradient(#3a9ee8,#1f7fd0);color:var(--white);font-size:17px;padding-top:10px}
.premium-col .price{height:61px;background:radial-gradient(ellipse at center,#56b8f3,#1a77cf);color:var(--white);font-size:24px;font-weight:700;padding-top:17px}
.premium-col .prow{height:35px;font-size:12px;padding-top:10px;color:var(--orange-dark);font-weight:700}
.premium-col .prow:nth-child(odd){background:#f7f7f7}
.premium-col .prow:nth-child(even){background:#e9e9e9}
.premium-col .prow.t{color:#444;font-weight:400}
.btn{display:inline-flex;align-items:center;justify-content:space-between;width:150px;height:24px;background:linear-gradient(#3a3a3a,#111);border-radius:4px;color:var(--white);font-size:12px;font-weight:400;padding-left:18px;overflow:hidden}
.btn .go{width:34px;height:24px;background:var(--blue);display:flex;align-items:center;justify-content:center}
.req{left:122px;top:1138px;font-size:11px;color:#666}

/* transaction band */
.tcband{left:0;top:1175px;width:1200px;height:163px;background:var(--band)}
.tcband h3{position:absolute;left:118px;top:22px;font-size:22px;font-weight:400;color:var(--blue)}
.tcband .arrow{position:absolute;left:118px;top:54px}
.tcband .big{position:absolute;left:118px;top:52px;font-size:74px;line-height:88px;font-weight:700;color:var(--orange);white-space:nowrap}
.tcband p{position:absolute;left:563px;top:64px;width:500px;font-size:15px;line-height:36px;color:#666}

/* listing includes */
.section-title{font-size:22px;color:var(--blue);font-weight:400}
.includes-title{left:118px;top:1366px}
.card{width:459px;height:113px;border:2px solid #cfcfcf;background:var(--white)}
.card .t{position:absolute;left:18px;top:12px;font-size:17px;color:var(--blue)}
.card .p{position:absolute;left:18px;top:42px;font-size:18px;color:var(--orange)}
.card .meta{position:absolute;left:18px;top:78px;display:flex;gap:16px;font-size:11px;color:#666;align-items:center}
.card .meta span{display:flex;align-items:center;gap:6px}
.card .photo{position:absolute;top:-1px;width:115px;height:115px;border-radius:50%;border:4px solid #e2e2e2}
.card.left .photo{right:12px}
.card.right .photo{left:-1px}
.card.right .t,.card.right .p,.card.right .meta{left:156px}

/* additional services */
.services{left:118px;top:1854px;width:964px;border:1px solid var(--line)}
.services .head{height:44px;background:var(--navy);color:var(--white);font-size:23px;padding:8px 20px}
.services .note{height:38px;font-size:11px;color:#777;padding:12px 16px}
.services .q{height:42px;background:#d9d9d9;font-size:18px;color:#444;padding:9px 20px;display:flex;align-items:center;gap:16px}
.services .q i{width:10px;height:10px;background:var(--blue)}
.svc-row{display:flex;height:35px;font-size:12px;color:#666}
.svc-row div{padding-top:10px}
.svc-row .n{width:460px;padding-left:14px}
.svc-row .pr{width:250px;text-align:center}
.svc-row .a{width:252px;text-align:center;color:#333}
.svc-row.top{background:var(--blue);color:var(--white);font-weight:700;font-size:14px}
.svc-row.top .a{border-left:1px solid var(--white)}
.svc-row.odd .n{background:#f3f3f3}.svc-row.odd .pr{background:#eaf0f8}.svc-row.odd .a{background:#dde6f1}
.svc-row.even .n{background:#dedede}.svc-row.even .pr{background:#d6dce4}.svc-row.even .a{background:#cdd6e1}

/* browse */
.browse{left:0;top:2194px;width:1200px;height:348px;background:#efefef}
.browse h4{position:absolute;top:28px;font-size:25px;font-weight:700;color:#222}
.city-col{position:absolute;top:92px;font-size:13px;line-height:24px;color:#666;list-style:none}
.viewall{position:absolute;left:54px;top:245px;font-size:15px;color:var(--blue);font-weight:500}
.video{position:absolute;left:829px;top:72px;width:314px;height:203px;background:linear-gradient(#8fb4d8,#5a7d52 70%,#3f5f3a)}
.video .play{position:absolute;left:92px;top:90px;color:var(--white);font-weight:700;font-size:15px;display:flex;align-items:center;gap:6px}
.video .play i{width:18px;height:18px;border-radius:50%;background:var(--orange)}

/* footer */
.silhouette{left:0;top:2542px;width:1200px;height:48px;background:linear-gradient(#efefef,#1e5aa6 85%)}
.footer{left:0;top:2590px;width:1200px;height:220px;background:var(--blue)}
.flinks{position:absolute;top:60px;list-style:none;font-size:12px;color:var(--white)}
.flinks li{height:24px;border-bottom:1px solid rgba(255,255,255,.25);width:170px;padding-top:4px;white-space:nowrap}
.newsletter{position:absolute;left:805px;top:62px;font-size:11px;color:var(--white)}
.newsletter .input{position:absolute;left:0;top:18px;width:300px;height:38px;background:var(--white)}
.newsletter .send{position:absolute;left:300px;top:18px;width:38px;height:38px;background:var(--orange);display:flex;align-items:center;justify-content:center}
.social{position:absolute;left:805px;top:146px;display:flex;gap:10px}
.social i{width:30px;height:30px;background:var(--deep);display:block}
.bottom{left:0;top:2810px;width:1200px;height:56px;background:var(--deep);color:#c9d6ea;font-size:11px;display:flex;align-items:center;justify-content:space-between;padding:0 56px}
</style>
</head>
<body>

<nav class="abs topbar">
  <div class="menu"><span>Search Listings</span><span>Why Choose Brivo</span><span>Directory</span><span>Guides</span></div>
  <span class="phone">+ 305-555-0187</span>
  <span class="help">FAQ's / Contact Us / Help</span>
</nav>

<header class="abs header">
  <div class="abs brand"><span class="mark"></span>Brivo Real Estate</div>
  <div class="abs user"><span class="avatar" role="img" aria-label="User profile photo"></span>MARCUS L.<span class="caret"></span></div>
</header>

<section class="abs titleband">
  <div class="skyline" role="img" aria-label="Pale blue city skyline"></div>
  <h1 class="cond">PAACKAGE</h1>
</section>

<section class="abs box pay">
  <h2 class="cond">Packages &amp; Pricing</h2>
  <div class="zero cond">$0</div>
  <div class="note cond">Pay Noting<br>Until Home<br>Slod</div>
</section>

<section class="abs box save">
  <h2 class="cond">Maximum Market Exposure Gurannted!</h2>
  <div class="q">How much will you save?</div>
  <div class="field" style="left:24px">$</div>
  <div class="field" style="left:287px">My Savings</div>
  <div class="hint">Enter Estimated Sales Price</div>
</section>

<section class="abs banner">
  <svg width="962" height="105" viewBox="0 0 962 105">
    <polygon points="0,0 242,0 262,52 242,105 0,105" fill="#f08a2c"/>
    <polygon points="252,0 592,0 612,52 592,105 252,105 272,52" fill="#1d59a6"/>
    <polygon points="600,0 962,0 962,105 600,105 620,52" fill="#1d59a6"/>
    <polyline points="588,0 608,52 588,105" fill="none" stroke="#fff" stroke-width="4"/>
  </svg>
  <div class="cell best cond">Best Value</div>
  <div class="cell cond" style="left:262px;width:340px"><span class="plan">Basic $179</span><span class="fee">+ Transction coordintation fee $299</span></div>
  <div class="cell cond" style="left:612px;width:350px"><span class="plan">Primium $249</span><span class="fee">+ Transction coordintation fee $299</span></div>
</section>

<section class="abs compare">
  <div class="head">MOST POPULAR</div>
  <div class="col-head" style="left:417px"><div class="name">Basic</div><div class="price">$199</div></div>
  <div class="col-head" style="left:779px"><div class="name">MLS</div><div class="price">$499</div></div>
  <div class="rows">
    <div class="row"><div class="label">Listing on brivo.example</div><div class="c">✕</div><div class="c"></div><div class="c">✕</div></div>
    <div class="row"><div class="label">Earn Featured listing on homeportal.example</div><div class="c">✕</div><div class="c"></div><div class="c">✕</div></div>
    <div class="row"><div class="label">Photos</div><div class="c t">6</div><div class="c"></div><div class="c t">Unlimited</div></div>
    <div class="row"><div class="label">Free Brokers Price Opinion</div><div class="c"></div><div class="c"></div><div class="c">✕</div></div>
    <div class="row"><div class="label">Exposure on over 50+ real estate website including Homefinder Nestlist</div><div class="c"></div><div class="c"></div><div class="c">✕</div></div>
    <div class="row"><div class="label">Ptrmium Yard Sing With Mobile ID #</div><div class="c"></div><div class="c"></div><div class="c">✕</div></div>
    <div class="row"><div class="label">Listing on local MLS</div><div class="c"></div><div class="c"></div><div class="c">✕</div></div>
    <div class="row" style="background:#fff;height:39px"><div class="label"></div>
      <div class="c" style="padding-top:6px"><span class="btn">Get started<span class="go"><svg width="16" height="10"><path d="M1 1l5 4-5 4M8 1l5 4-5 4" stroke="#fff" stroke-width="2" fill="none"/></svg></span></span></div>
      <div class="c"></div>
      <div class="c" style="padding-top:6px"><span class="btn">Get started<span class="go"><svg width="16" height="10"><path d="M1 1l5 4-5 4M8 1l5 4-5 4" stroke="#fff" stroke-width="2" fill="none"/></svg></span></span></div>
    </div>
  </div>
</section>

<div class="abs premium-col">
  <div class="name">Preimum</div>
  <div class="price">$249</div>
  <div>
    <div class="prow">✕</div><div class="prow">✕</div><div class="prow t">Unlimited</div><div class="prow">✕</div><div class="prow">✕</div><div class="prow">✕</div><div class="prow"></div>
  </div>
  <div style="padding-top:8px"><span class="btn">Get started<span class="go"><svg width="16" height="10"><path d="M1 1l5 4-5 4M8 1l5 4-5 4" stroke="#fff" stroke-width="2" fill="none"/></svg></span></span></div>
</div>

<div class="abs req">* This Requires a 3% Buyers Agent Commision.</div>

<section class="abs tcband">
  <h3 class="cond">Transaction Coordinator Fees</h3>
  <svg class="arrow" width="425" height="88" viewBox="0 0 425 88"><polygon points="0,0 390,0 425,44 390,88 0,88" fill="#f6f6f6"/></svg>
  <div class="big cond">NO WORRIES</div>
  <p>As the transaction cooriditors, Brivo Real Estatewill guide the buyer and seller though the entire transaction in an efficient and worry free way.</p>
</section>

<h3 class="abs section-title includes-title cond">All Listing Indulced</h3>

<div class="abs card left" style="left:118px;top:1416px"><div class="t">Only Pre Approved Byuers</div><div class="p">$179,000</div>
  <div class="meta"><span><svg width="20" height="12"><path d="M1 11V5l9-4 9 4v6M4 11V7h12v4" stroke="#777" fill="none"/></svg>1 Garage</span><span><svg width="20" height="12"><path d="M1 11V2M1 8h18v3M4 7V5h6v2" stroke="#777" fill="none"/></svg>2 Beds</span><span><svg width="20" height="12"><path d="M1 6h18M3 6v3q0 2 3 2h8q3 0 3-2V6M3 6V1h3" stroke="#777" fill="none"/></svg>2 Baths</span></div>
  <div class="photo" role="img" aria-label="Home interior with staircase" style="background:linear-gradient(#b0603e,#5a2a1a)"></div></div>
<div class="abs card right" style="left:623px;top:1416px"><div class="t">Sechedule Open House</div><div class="p">$349,000</div>
  <div class="meta"><span><svg width="20" height="12"><path d="M1 11V5l9-4 9 4v6M4 11V7h12v4" stroke="#777" fill="none"/></svg>1 Garage</span><span><svg width="20" height="12"><path d="M1 11V2M1 8h18v3M4 7V5h6v2" stroke="#777" fill="none"/></svg>2 Beds</span><span><svg width="20" height="12"><path d="M1 6h18M3 6v3q0 2 3 2h8q3 0 3-2V6M3 6V1h3" stroke="#777" fill="none"/></svg>2 Baths</span></div>
  <div class="photo" role="img" aria-label="Bright living room" style="background:linear-gradient(#d9c9b0,#8a6c50)"></div></div>

<div class="abs card left" style="left:118px;top:1556px"><div class="t">Customer support</div><div class="p">$249,000</div>
  <div class="meta"><span><svg width="20" height="12"><path d="M1 11V5l9-4 9 4v6M4 11V7h12v4" stroke="#777" fill="none"/></svg>1 Garage</span><span><svg width="20" height="12"><path d="M1 11V2M1 8h18v3M4 7V5h6v2" stroke="#777" fill="none"/></svg>2 Beds</span><span><svg width="20" height="12"><path d="M1 6h18M3 6v3q0 2 3 2h8q3 0 3-2V6M3 6V1h3" stroke="#777" fill="none"/></svg>2 Baths</span></div>
  <div class="photo" role="img" aria-label="Modern house exterior" style="background:linear-gradient(#9fb6c8,#5a4332)"></div></div>
<div class="abs card right" style="left:623px;top:1556px"><div class="t">Contract Negotiation support</div><div class="p">$299,000</div>
  <div class="meta"><span><svg width="20" height="12"><path d="M1 11V5l9-4 9 4v6M4 11V7h12v4" stroke="#777" fill="none"/></svg>1 Garage</span><span><svg width="20" height="12"><path d="M1 11V2M1 8h18v3M4 7V5h6v2" stroke="#777" fill="none"/></svg>2 Beds</span><span><svg width="20" height="12"><path d="M1 6h18M3 6v3q0 2 3 2h8q3 0 3-2V6M3 6V1h3" stroke="#777" fill="none"/></svg>2 Baths</span></div>
  <div class="photo" role="img" aria-label="Kitchen interior" style="background:linear-gradient(#cfcac4,#6b5a4a)"></div></div>

<div class="abs card left" style="left:118px;top:1695px"><div class="t">Listing Stat Tracking</div><div class="p">$499,000</div>
  <div class="meta"><span><svg width="20" height="12"><path d="M1 11V5l9-4 9 4v6M4 11V7h12v4" stroke="#777" fill="none"/></svg>1 Garage</span><span><svg width="20" height="12"><path d="M1 11V2M1 8h18v3M4 7V5h6v2" stroke="#777" fill="none"/></svg>2 Beds</span><span><svg width="20" height="12"><path d="M1 6h18M3 6v3q0 2 3 2h8q3 0 3-2V6M3 6V1h3" stroke="#777" fill="none"/></svg>2 Baths</span></div>
  <div class="photo" role="img" aria-label="Kitchen with red cabinets" style="background:linear-gradient(#e4ddd6,#8c3a30)"></div></div>
<div class="abs card right" style="left:623px;top:1695px"><div class="t">Step by Step Guides &amp; tools</div><div class="p">$449,000</div>
  <div class="meta"><span><svg width="20" height="12"><path d="M1 11V5l9-4 9 4v6M4 11V7h12v4" stroke="#777" fill="none"/></svg>1 Garage</span><span><svg width="20" height="12"><path d="M1 11V2M1 8h18v3M4 7V5h6v2" stroke="#777" fill="none"/></svg>2 Beds</span><span><svg width="20" height="12"><path d="M1 6h18M3 6v3q0 2 3 2h8q3 0 3-2V6M3 6V1h3" stroke="#777" fill="none"/></svg>2 Baths</span></div>
  <div class="photo" role="img" aria-label="Dining room interior" style="background:linear-gradient(#eee2cc,#a08460)"></div></div>

<section class="abs services">
  <div class="head cond">Additional Services Offered</div>
  <div class="note">* Payment Due When Services is Completed</div>
  <div class="q cond">Will you offer a 3% buyers agent Commission? <i></i></div>
  <div class="svc-row top"><div class="n">Services</div><div class="pr">Price</div><div class="a"></div></div>
  <div class="svc-row odd"><div class="n">Photofeesional Photographyh</div><div class="pr">$xxxx</div><div class="a">Add</div></div>
  <div class="svc-row even"><div class="n">Profesiol House stageing</div><div class="pr">$xxxx</div><div class="a">Add</div></div>
  <div class="svc-row odd"><div class="n">Broker Price opinion</div><div class="pr">$xxxx</div><div class="a">Add</div></div>
  <div class="svc-row even"><div class="n">Premium Yard sign</div><div class="pr">$xxxx</div><div class="a">Add</div></div>
</section>

<section class="abs browse">
  <h4 class="cond" style="left:54px">BROWSE BY CITIES</h4>
  <ul class="city-col" style="left:54px"><li>New york</li><li>Los Angles</li><li>Chicago</li><li>Miami</li><li>San Francisco</li><li>Denver</li></ul>
  <ul class="city-col" style="left:210px"><li>New york</li><li>Los Angles</li><li>Chicago</li><li>Miami</li><li>San Francisco</li><li>Denver</li></ul>
  <ul class="city-col" style="left:367px"><li>New york</li><li>Los Angles</li><li>Chicago</li><li>Miami</li><li>San Francisco</li><li>Denver</li></ul>
  <ul class="city-col" style="left:524px"><li>New york</li><li>Los Angles</li><li>Chicago</li><li>Miami</li><li>San Francisco</li><li>Denver</li></ul>
  <ul class="city-col" style="left:680px"><li>New york</li><li>Los Angles</li><li>Chicago</li><li>Miami</li><li>San Francisco</li><li>Denver</li></ul>
  <div class="viewall">VIEW ALL CITIES &nbsp;»</div>
  <h4 class="cond" style="left:829px">HOW IT WORKS</h4>
  <div class="video" role="img" aria-label="Video still of an agent in front of a house">
    <div class="play">WATCH VIDEO <i></i></div>
  </div>
</section>

<div class="abs silhouette" role="img" aria-label="City skyline silhouette"></div>

<footer class="abs footer">
  <ul class="flinks" style="left:54px"><li>About</li><li>Research</li><li>Services</li><li>Contact Us</li><li>Why Choose Us</li></ul>
  <ul class="flinks" style="left:296px"><li>Search Listings</li><li>Real Estate Guides</li><li>Neighborhood Info</li><li>Get Pre-Approved</li><li>Fair Housing Laws &amp; Information</li></ul>
  <ul class="flinks" style="left:531px"><li>Disclaimers</li><li>Feedback</li><li>Terms &amp; Conditions</li><li>Help</li></ul>
  <div class="newsletter">Enter your email adress to sign for our newsletter.
    <div class="input"></div>
    <div class="send"><svg width="18" height="14"><path d="M1 7h15M10 1l6 6-6 6" stroke="#fff" stroke-width="2.5" fill="none"/></svg></div>
  </div>
  <div class="social"><i></i><i></i><i></i><i></i><i></i></div>
</footer>

<div class="abs bottom"><span>© 2014 Brivo Real Estate &nbsp;|&nbsp; All rights reserved.</span><span>Powered by Norvale Web Studio</span></div>

</body>
</html>
```